Update Old OR create new Website

Current Website is looking a bit old, I did this one a few years back.

Would like a fresh new look, current website sitepress theme is " the Vanta theme" from plumcrate and I just purchased this theme - "bravlo" also from plumcrate, I quite like the look of - http://bravlo.quorvex-skins.com/tech-business/ and if we could get somthing simlar would be great.

current website is at http://www.hle.com.au, have been playing around with the slider that i like.

I have said 5 pages to be designed but really it is just a 5 page website where most pages will look the same.

Any questions please let me know

Target Market(s)

Business

Coding

Coded - Design and coding required

Number of Pages Required

5+ page

Font styles to use
Sans Serif

Colors
33a6d7
0292cd
ffffff
0255a3

Requirements
Must have
• Device compatibility - pc, tablet, phone
Nice to have
• video
Should not have
• vunerabilities. Must also use images that will expire or disappear, ie must be uploaded to site not links to elsewhere.

```html
<!DOCTYPE html>
<html lang="en">
<head>
<meta charset="utf-8">
<title>Tech Business</title>
<link href="https://fonts.googleapis.com/css2?family=Poppins:wght@300;400;500&display=swap" rel="stylesheet">
<style>
:root{
  --blue:#0292cd;
  --blue-light:#33a6d7;
  --white:#ffffff;
  --ink:#222222;
  --grey:#8a8a8a;
  --dark:#2b2b2b;
  --panel:#232323;
  --field:#d9d9d9;
  --bar:#111111;
}
*{margin:0;padding:0;box-sizing:border-box}
html,body{width:1200px;height:1200px;overflow:hidden;background:var(--white);font-family:'Poppins',sans-serif}
.page{position:relative;width:1200px;height:1200px}
.abs{position:absolute}

/* services slider */
.service-card{position:absolute;top:50px;width:213px;height:261px}
.card-code{left:150px;background:linear-gradient(160deg,#0d1a2c,#0a1220 55%,#1a2a4a)}
.card-laptop{left:379px;background:linear-gradient(150deg,#d8d6d2,#c7c5c1 45%,#f1f0ee)}
.card-phone{left:607px;background:linear-gradient(140deg,#6b4a30,#b88a63 50%,#4a3325)}
.card-devices{left:836px;background:linear-gradient(180deg,#cfd3d8,#eef0f2)}
.card-overlay{position:absolute;inset:0;display:flex;flex-direction:column;align-items:center;justify-content:center;text-align:center;padding:0 24px}
.card-title{color:var(--blue-light);font-size:21px;font-weight:400;margin-bottom:12px}
.card-text{color:#e8e8e8;font-size:10.5px;font-weight:300;line-height:15px;text-align:justify;text-align-last:center}
.card-link{color:var(--blue-light);font-size:10px;margin-top:14px}

.slider-arrow{position:absolute}

/* testimonials */
.testimonials{position:absolute;left:0;top:420px;width:1200px;height:474px;
  background:radial-gradient(ellipse at 18% 60%,#4a3a33 0%,#333 40%,var(--dark) 70%)}
.quote-box{position:absolute;top:57px;width:260px;height:206px;background:var(--panel);opacity:.95}
.quote-box::after{content:"";position:absolute;left:40px;bottom:-20px;border-left:20px solid transparent;border-right:20px solid transparent;border-top:20px solid var(--panel)}
.quote-title{position:absolute;left:36px;top:33px;color:var(--blue-light);font-size:17px;font-weight:400}
.quote-text{position:absolute;left:37px;top:68px;width:200px;color:#f0f0f0;font-size:11.5px;font-weight:300;line-height:18.7px}
.avatar{position:absolute;top:297px;width:72px;height:72px;border-radius:50%;background:linear-gradient(160deg,#c9c9c9,#6e6e6e)}
.person{position:absolute;top:318px}
.person-name{color:var(--white);font-size:17px;font-weight:300;line-height:20px}
.person-role{color:var(--blue-light);font-size:13.5px;font-weight:300}

/* footer */
.footer-heading{position:absolute;top:974px;color:var(--ink);font-size:15px;font-weight:400;letter-spacing:.3px}
.contact-line{position:absolute;left:150px;display:flex;gap:6px;color:var(--grey);font-size:9.5px;font-weight:300;line-height:14px}
.menu-list{position:absolute;top:1014px;list-style:none}
.menu-list li{font-size:9px;color:var(--grey);line-height:16.5px;display:flex;align-items:center;gap:8px;text-transform:uppercase}
.menu-list li.active{color:var(--blue)}
.menu-list svg{flex:none}
.field{position:absolute;left:672px;width:163px;height:26px;background:var(--field);color:#8e8e8e;font-size:9.5px;padding-left:16px;line-height:26px}
.send-btn{position:absolute;left:672px;top:1083px;width:57px;height:20px;background:var(--blue);color:var(--white);font-size:9.5px;text-align:center;line-height:20px}
.social{position:absolute;top:1015px;width:23px;height:23px;border:1px solid #c6c6c6;border-radius:50%}
.social::after{content:"";position:absolute;left:8px;top:8px;width:5px;height:5px;border-radius:50%;background:#9a9a9a}
.legal-bar{position:absolute;left:0;top:1167px;width:1200px;height:33px;background:var(--bar);color:var(--white);font-size:9.5px;text-align:center;line-height:33px;font-weight:300}
</style>
</head>
<body>
<div class="page">

  <!-- services slider -->
  <div class="service-card card-code" role="img" aria-label="Photo of program code on a dark screen">
    <div class="card-overlay">
      <div class="card-title">SEO &amp; Analytics</div>
      <div class="card-text">It is a long established fact that a reader will be distracted by the readable content of a page when looking at its layout.</div>
      <div class="card-link">Read More &rsaquo;</div>
    </div>
  </div>
  <div class="service-card card-laptop" role="img" aria-label="Photo of a laptop and tablet showing charts"></div>
  <div class="service-card card-phone" role="img" aria-label="Photo of a hand holding a smartphone with apps"></div>
  <div class="service-card card-devices" role="img" aria-label="Mockup of a website on desktop, tablet and phone screens"></div>

  <svg class="slider-arrow" style="left:531px;top:341px" width="38" height="38" viewBox="0 0 38 38"><circle cx="19" cy="19" r="18" fill="none" stroke="#222" stroke-width="1.5"/><path d="M23 11 L13 19 L23 27 Z" fill="none" stroke="#222" stroke-width="1.5" stroke-linejoin="round"/></svg>
  <svg class="slider-arrow" style="left:621px;top:341px" width="38" height="38" viewBox="0 0 38 38"><circle cx="19" cy="19" r="18" fill="none" stroke="#222" stroke-width="1.5"/><path d="M15 11 L25 19 L15 27 Z" fill="none" stroke="#222" stroke-width="1.5" stroke-linejoin="round"/></svg>

  <!-- testimonials -->
  <section class="testimonials" role="img" aria-label="Background photo of hands typing on a keyboard beside a wristwatch, darkened">
    <div class="quote-box" style="left:150px">
      <div class="quote-title">Lorem Ipsum</div>
      <p class="quote-text">Contrary to popular belief, Lorem Ipsum is not simply random text. It has roots in a piece of classical Latin literature from 45 BC, making it over 2000 years old.</p>
    </div>
    <div class="quote-box" style="left:471px">
      <div class="quote-title" style="top:39px">Lorem Ipsum</div>
      <p class="quote-text" style="top:74px">Contrary to popular belief, Lorem Ipsum is not simply random text. It has roots in a piece of classical Latin literature from 45 BC, making it over 2000 years old.</p>
    </div>
    <div class="quote-box" style="left:791px">
      <div class="quote-title" style="top:34px">Lorem Ipsum</div>
      <p class="quote-text">Contrary to popular belief, Lorem Ipsum is not simply random text. It has roots in a piece of classical Latin literature from 45 BC, making it over 2000 years old.</p>
    </div>

    <div class="avatar" style="left:151px" role="img" aria-label="Portrait photo of Marek Holloway"></div>
    <div class="person" style="left:246px"><div class="person-name">Marek Holloway</div><div class="person-role">Manager</div></div>
    <div class="avatar" style="left:470px" role="img" aria-label="Portrait photo of Jonas Revelle"></div>
    <div class="person" style="left:567px"><div class="person-name">Jonas Revelle</div><div class="person-role">CEO</div></div>
    <div class="avatar" style="left:791px" role="img" aria-label="Portrait photo of Teo Brandvik"></div>
    <div class="person" style="left:887px"><div class="person-name">Teo Brandvik</div><div class="person-role">Co. Manager</div></div>

    <svg class="slider-arrow" style="left:531px;top:403px" width="38" height="38" viewBox="0 0 38 38"><circle cx="19" cy="19" r="18" fill="none" stroke="#fff" stroke-width="1.5"/><path d="M23 11 L13 19 L23 27 Z" fill="none" stroke="#fff" stroke-width="1.5" stroke-linejoin="round"/></svg>
    <svg class="slider-arrow" style="left:621px;top:403px" width="38" height="38" viewBox="0 0 38 38"><circle cx="19" cy="19" r="18" fill="none" stroke="#fff" stroke-width="1.5"/><path d="M15 11 L25 19 L15 27 Z" fill="none" stroke="#fff" stroke-width="1.5" stroke-linejoin="round"/></svg>
  </section>

  <!-- footer -->
  <div class="footer-heading" style="left:150px">CONTACT US</div>
  <div class="footer-heading" style="left:416px">MENU</div>
  <div class="footer-heading" style="left:672px">NEWSLETTER</div>
  <div class="footer-heading" style="left:942px">FOLLOW US:</div>

  <div class="contact-line" style="top:1013px">
    <svg width="9" height="12" viewBox="0 0 9 12"><path d="M4.5 11.5 C2 8 1 6.3 1 4.5 A3.5 3.5 0 0 1 8 4.5 C8 6.3 7 8 4.5 11.5 Z" fill="none" stroke="#aaa"/><circle cx="4.5" cy="4.5" r="1.2" fill="none" stroke="#aaa"/></svg>
    <span>Lorem Ipsum is simply dummy text of<br>the typesetting industry.</span>
  </div>
  <div class="contact-line" style="top:1054px">
    <svg width="10" height="12" viewBox="0 0 10 12"><path d="M2 2 L4 1.5 L5 4 L3.8 5 C4.3 6.5 5 7.4 6.3 8.2 L7.3 7 L9.5 8.3 L9 10.3 C5 10.5 1.5 6.5 2 2 Z" fill="none" stroke="#aaa" stroke-width=".9"/></svg>
    <span>(123) 555-0148</span>
  </div>
  <div class="contact-line" style="top:1072px">
    <svg width="10" height="12" viewBox="0 0 10 12"><rect x=".5" y="3" width="9" height="7" fill="none" stroke="#aaa"/><path d="M.5 3 L5 7 L9.5 3" fill="none" stroke="#aaa"/></svg>
    <span>info@postlane.com</span>
  </div>

  <ul class="menu-list" style="left:416px">
    <li class="active"><svg width="5" height="7" viewBox="0 0 5 7"><path d="M1 1 L4 3.5 L1 6" fill="none" stroke="#0292cd" stroke-width="1.2"/></svg>Home</li>
    <li><svg width="5" height="7" viewBox="0 0 5 7"><path d="M1 1 L4 3.5 L1 6" fill="none" stroke="#555" stroke-width="1.2"/></svg>Servers</li>
    <li><svg width="5" height="7" viewBox="0 0 5 7"><path d="M1 1 L4 3.5 L1 6" fill="none" stroke="#555" stroke-width="1.2"/></svg>Networks</li>
    <li><svg width="5" height="7" viewBox="0 0 5 7"><path d="M1 1 L4 3.5 L1 6" fill="none" stroke="#555" stroke-width="1.2"/></svg>Managed IT</li>
  </ul>
  <ul class="menu-list" style="left:513px">
    <li><svg width="5" height="7" viewBox="0 0 5 7"><path d="M1 1 L4 3.5 L1 6" fill="none" stroke="#555" stroke-width="1.2"/></svg>Web</li>
    <li><svg width="5" height="7" viewBox="0 0 5 7"><path d="M1 1 L4 3.5 L1 6" fill="none" stroke="#555" stroke-width="1.2"/></svg>App's</li>
    <li><svg width="5" height="7" viewBox="0 0 5 7"><path d="M1 1 L4 3.5 L1 6" fill="none" stroke="#555" stroke-width="1.2"/></svg>Internet</li>
    <li><svg width="5" height="7" viewBox="0 0 5 7"><path d="M1 1 L4 3.5 L1 6" fill="none" stroke="#555" stroke-width="1.2"/></svg>Contact</li>
  </ul>

  <div class="field" style="top:1014px">Name</div>
  <div class="field" style="top:1048px">Email</div>
  <div class="send-btn">Send</div>

  <div class="social" style="left:943px" aria-label="Social link one"></div>
  <div class="social" style="left:972px" aria-label="Social link two"></div>
  <div class="social" style="left:1000px" aria-label="Social link three"></div>
  <div class="social" style="left:1028px" aria-label="Social link four"></div>

  <div class="legal-bar">All Rights Reserved Terms of Use and Privacy Policy</div>
</div>
</body>
</html>
```